Mobile Oil Change company needs a flyer to promote new business

We need a flyer to 1) print & handout and 2) email out to potential customers. We are a mobile oil change company that comes to our customer locations to perform the work instead of customers going to traditional oil change companies. We have a 21 point inspection with our oil change. (21 point inspection details will not be on the flyer). Would like to keep the flyer simple but creative. I'm attaching 1) the write-up we created, 2) our logo (logo color is dark teal on white but other combinations are included if you wanted to propose a different color combination), and 3) additional services we offer. Logo font is Alegreya Sans.
Would like the additional services listed with icons and brief descriptions (similar to attachment) without pricing. Company website for reference is www.brookmerelubeworks.com.

Target Market(s)

Companies with many service vehicles such as Oil & Gas service companies, heating and air conditioning companies, utility companies, police departments, etc. Companies that prioritize convenience and maintenance first.

Font styles to use
Sans Serif

Colors
00a990

Requirements
Must have
• Simple but creative design with our logo at top of the flyer. Additional Services (details in document supplied) can be smaller and less prominent than other "main" content listed in the CONTENT document supplied.
Should not have
• Do not use animated character graphics in the flyer and limit (1) stock photos to A small area in the flyer.

```html
<!DOCTYPE html>
<html lang="en">
<head>
<meta charset="utf-8">
<title>Brookmere Lubeworks – Mobile Oil Change Flyer</title>
<link href="https://fonts.googleapis.com/css2?family=Roboto+Condensed:wght@400;700&family=Roboto:wght@400&display=swap" rel="stylesheet">
<style>
  :root{
    --teal:#00a990;
    --deep:#0e2f33;
    --pine:#17494e;
    --mid:#135257;
    --ink:#124a4f;
    --text:#454545;
    --muted:#6a6a6a;
    --page:#727272;
    --white:#ffffff;
  }
  *{box-sizing:border-box;margin:0;padding:0}
  html,body{width:981px;height:1200px;overflow:hidden;background:var(--page)}
  body{position:relative;font-family:"Roboto Condensed",sans-serif}
  .flyer{
    position:absolute;left:157px;top:112px;width:827px;height:1169px;
    background:var(--white);overflow:hidden;
    transform:scale(0.8314);transform-origin:0 0;
    box-shadow:8px 8px 10px rgba(0,0,0,.45);
  }
  .sweep{position:absolute;left:0;top:0;width:827px;height:760px}
  .brand{
    position:absolute;left:44px;top:90px;width:368px;height:150px;
    background:var(--white);border-radius:0 18px 40px 0;
    display:flex;flex-direction:column;justify-content:center;padding-left:48px;
  }
  .brand-name{font-weight:700;color:var(--ink);font-size:52px;line-height:1;letter-spacing:1px}
  .brand-sub{font-weight:700;color:var(--ink);font-size:28px;letter-spacing:6px;margin-top:8px}
  .headline{position:absolute;left:457px;top:92px;color:var(--white);font-weight:700;text-transform:uppercase;line-height:.95}
  .headline span{display:block;font-size:51px}
  .headline span.small{font-size:42px;margin-top:2px}
  .intro{position:absolute;left:46px;top:298px;width:340px;color:var(--teal);font-size:25px;line-height:29px}
  .steps{position:absolute;left:44px;top:405px;list-style:none;color:var(--text);font-size:23.5px;line-height:29.5px;white-space:nowrap}
  .steps b{color:var(--teal);font-weight:400;display:inline-block;width:28px}
  .highlights{
    position:absolute;left:44px;top:582px;width:740px;height:78px;border-radius:8px;
    background:var(--pine);color:var(--white);list-style:none;padding:9px 0 0 26px;
    font-weight:700;font-size:24px;line-height:29px;white-space:nowrap;
  }
  .highlights li{display:flex;align-items:center;gap:10px}
  .drop{width:13px;height:18px;flex:none}
  .section-title{position:absolute;left:44px;width:740px;display:flex;align-items:center;gap:8px;color:var(--ink);font-weight:700;font-size:30px;white-space:nowrap}
  .section-title::before,.section-title::after{content:"";flex:1;height:2px;background:var(--ink)}
  .section-title .drop{width:20px;height:30px}
  .services-title{top:683px}
  .contact-title{top:963px}
  .services{position:absolute;left:54px;top:742px;width:740px;display:grid;grid-template-columns:353px 380px;row-gap:18px}
  .service{display:flex;gap:17px;height:54px}
  .service svg{width:50px;height:50px;flex:none;margin-top:2px}
  .service h3{color:var(--teal);font-weight:400;font-size:18.5px;line-height:22px;text-transform:uppercase;white-space:nowrap}
  .service p{font-family:"Roboto",sans-serif;color:var(--muted);font-size:12.8px;line-height:16px;white-space:nowrap}
  .contact{position:absolute;top:1027px;display:flex;align-items:center;gap:14px;white-space:nowrap}
  .contact-call{left:73px}
  .contact-mail{left:360px}
  .contact-icon{width:64px;height:64px;flex:none;border-radius:6px;background:var(--pine);display:flex;align-items:center;justify-content:center}
  .contact-icon svg{width:34px;height:34px}
  .contact h4{color:var(--ink);font-weight:700;font-size:27px;line-height:29px}
  .contact p{color:var(--ink);font-size:27px;line-height:29px}
  .contact-mail p{font-size:25.5px}
  .site{position:absolute;left:0;bottom:0;width:827px;height:39px;background:var(--pine);color:var(--white);text-align:center;font-size:23px;line-height:39px;letter-spacing:5px;white-space:nowrap}
</style>
</head>
<body>
<main class="flyer">
  <svg class="sweep" viewBox="0 0 827 760" aria-hidden="true">
    <path fill="var(--teal)" d="M0,0 H827 V730 C800,540 700,390 520,318 C420,280 330,270 280,258 C140,225 50,130 0,18 Z"/>
    <path fill="var(--mid)" d="M0,0 H827 V718 C800,530 700,375 520,305 C420,268 330,258 280,246 C140,215 55,120 0,10 Z"/>
    <path fill="var(--deep)" d="M0,0 H827 V705 C800,515 700,360 520,290 C420,255 330,246 280,234 C140,205 60,110 0,0 Z"/>
  </svg>

  <header class="brand">
    <div class="brand-name">BROOKMERE</div>
    <div class="brand-sub">LUBEWORKS</div>
  </header>

  <h1 class="headline"><span>Hassle Free</span><span>Oil Changes</span><span class="small">On Your Terms</span></h1>

  <p class="intro">Our simple 5-step process lets you schedule an appointment and save time &amp; money</p>

  <ol class="steps">
    <li><b>1)</b>Call or email us to schedule service</li>
    <li><b>2)</b>Our highly trained technicians come to you for service</li>
    <li><b>3)</b>Service is performed quickly on your vehicle</li>
    <li><b>4)</b>Pay agreed-upon pricing and receipt is emailed to you</li>
    <li><b>5)</b>Services performed are tracked electronically &amp; reminders created</li>
  </ol>

  <ul class="highlights">
    <li><svg class="drop" viewBox="0 0 20 30"><path fill="var(--teal)" d="M10,0 C14,10 20,15 20,20 A10,10 0 0 1 0,20 C0,15 6,10 10,0Z"/></svg>High quality synthetic oil used is best suited for commercial vehicles</li>
    <li><svg class="drop" viewBox="0 0 20 30"><path fill="var(--teal)" d="M10,0 C14,10 20,15 20,20 A10,10 0 0 1 0,20 C0,15 6,10 10,0Z"/></svg>Service includes a 21-point inspection</li>
  </ul>

  <h2 class="section-title services-title"><svg class="drop" viewBox="0 0 20 30"><path fill="var(--teal)" d="M10,0 C14,10 20,15 20,20 A10,10 0 0 1 0,20 C0,15 6,10 10,0Z"/></svg>ADDITIONAL SERVICES</h2>

  <section class="services">
    <article class="service">
      <svg viewBox="0 0 50 50" fill="none" stroke="var(--ink)" stroke-width="2.5"><rect x="2" y="4" width="46" height="42"/><path d="M14 4v42M36 4v42M2 13h12M2 21h12M2 29h12M2 37h12M36 13h12M36 21h12M36 29h12M36 37h12M18 10h14M18 18h14M18 26h14M18 34h14M18 42h14"/></svg>
      <div><h3>Engine Air Filter Replacement</h3><p>Maintain optimum engine performance.<br>Recommended every 15,000-30,000 miles.</p></div>
    </article>
    <article class="service">
      <svg viewBox="0 0 50 50" fill="none" stroke="var(--ink)" stroke-width="2.5"><path d="M10 8h24l8 6v32l-8-5H10l-6 4V12z"/><path d="M8 20c6-4 12 4 18 0s12 4 18 0M8 28c6-4 12 4 18 0s12 4 18 0M8 36c6-4 12 4 18 0"/></svg>
      <div><h3>Cabin Air Filter Replacement</h3><p>Maintain a clean A/C and fan system.<br>Recommended every 12 month or 15,000-25,000 miles.</p></div>
    </article>
    <article class="service">
      <svg viewBox="0 0 50 50" fill="none" stroke="var(--ink)" stroke-width="2.5"><path d="M3 22 C14 8 36 8 47 22 L27 40 Z"/><path d="M24 44 L14 16"/><circle cx="24" cy="44" r="2" fill="var(--ink)"/><path d="M18 4v3M25 2v3M32 4v3" stroke-dasharray="2 2"/></svg>
      <div><h3>Wiperblade Replacement</h3><p>Maintain Excellent visibility on the road.<br>Recommended every 6-12 month.</p></div>
    </article>
    <article class="service">
      <svg viewBox="0 0 50 50" fill="none" stroke="var(--ink)" stroke-width="2.5"><circle cx="25" cy="25" r="22"/><circle cx="25" cy="25" r="15"/><circle cx="25" cy="25" r="4"/><path d="M10 24h11M29 24h11M25 29v11"/></svg>
      <div><h3>Power Steering Fluid Flush</h3><p>Maintain proper power steering system health.<br>Recommended every 30,000-60,000 miles.</p></div>
    </article>
    <article class="service">
      <svg viewBox="0 0 50 50" fill="none" stroke="var(--ink)" stroke-width="2.5"><rect x="6" y="3" width="24" height="42" rx="3"/><rect x="11" y="9" width="14" height="10"/><path d="M2 47h32M30 16l8 6v16a3 3 0 0 0 6 0V20l-5-6"/></svg>
      <div><h3>Fuel System Treatment</h3><p>Clean your fuel system and injectors to<br>improve fuel economy.</p></div>
    </article>
    <article class="service">
      <svg viewBox="0 0 50 50" fill="none" stroke="var(--ink)" stroke-width="2.5"><circle cx="23" cy="27" r="20" stroke-dasharray="3 2"/><circle cx="23" cy="27" r="13"/><circle cx="23" cy="27" r="4"/><path d="M30 4a22 22 0 0 1 16 16"/></svg>
      <div><h3>Brake Fluid Flush</h3><p>Maintain an excellent functioning brake system.<br>Recommended every 2 year or 20,000 miles.</p></div>
    </article>
  </section>

  <h2 class="section-title contact-title"><svg class="drop" viewBox="0 0 20 30"><path fill="var(--teal)" d="M10,0 C14,10 20,15 20,20 A10,10 0 0 1 0,20 C0,15 6,10 10,0Z"/></svg>CONTACT US</h2>

  <div class="contact contact-call">
    <div class="contact-icon"><svg viewBox="0 0 24 24"><path fill="var(--teal)" d="M6.6 10.8a15.2 15.2 0 0 0 6.6 6.6l2.2-2.2a1 1 0 0 1 1-.25 11.4 11.4 0 0 0 3.6.57 1 1 0 0 1 1 1V20a1 1 0 0 1-1 1A17 17 0 0 1 3 4a1 1 0 0 1 1-1h3.5a1 1 0 0 1 1 1c0 1.25.2 2.45.57 3.57a1 1 0 0 1-.25 1z"/></svg></div>
    <div><h4>CALL NOW</h4><p>(833) 555-0148</p></div>
  </div>
  <div class="contact contact-mail">
    <div class="contact-icon"><svg viewBox="0 0 24 24"><path fill="var(--teal)" d="M2 5h20v14H2z"/><path fill="none" stroke="var(--pine)" stroke-width="1.6" d="M2 5l10 8 10-8M2 19l7-7M22 19l-7-7"/></svg></div>
    <div><h4>EMAIL US</h4><p>Sales@BrookmereLubeworks.com</p></div>
  </div>

  <footer class="site">WWW.BROOKMERELUBEWORKS.COM</footer>
</main>
</body>
</html>
```